" 816 " PACKAGING FOR AUTOMOTIVE SPAREPARTS PRODUCT

We need a zipped plastic packaging design for our product (i attached plastic packaging sample from another product). The plastic size is 40cm (length) * 30cm (width) with zipped on upside.

Our product is rubber parts for car suspension application. The brand is 816 and the slogan is 816 ORIGINAL PARTS ( see attached file).

We prefer the design use mostly red color (same color as our logo) and combine with other attracting color and it is on your control.
I have included a picture of packaging box that we currently use.

On the front side of the plastic packaging should have a view window that can view and see through the product inside the packaging.

The color and the design is on your control.
Updates

Project Deadline Extended
Reason: Hi I extend the deadline, create your Best design..

Target Market(s)

All customers, car workshop, retailer and user.

Industry/Entity Type

Automotive

Requirements
Must have
• - A space for labeling on front side of the packaging. (label size 4cm (lenght) * 7cm (width).
• - Should have the Pictures of our product on the packaging. I have included some pictures of our product, You can choose and put some of the pictures on the packaging.
• - The design should can communicate HIGH QUALITY PARTS.
Nice to have
• - Have some Blue print or silhouette (with a bit transparancy) of car spareparts item or workshop tool kit on the design.

```html
<!DOCTYPE html>
<html lang="en">
<head>
<meta charset="utf-8">
<title>816 Original Parts – Pouch Front</title>
<link href="https://fonts.googleapis.com/css2?family=Oswald:wght@400;600&family=Roboto+Condensed:wght@300;400&display=swap" rel="stylesheet">
<style>
  :root {
    --backdrop: #e4e9ec;
    --red-deep: #8c0e12;
    --red: #c4181d;
    --blue: #2356ad;
    --blue-deep: #163a80;
    --window-light: #d3d9df;
    --window: #b3bcc6;
    --white: #ffffff;
    --label-ink: #444a50;
  }
  html, body {
    margin: 0;
    padding: 0;
    width: 1200px;
    height: 1200px;
    overflow: hidden;
    background: var(--backdrop);
  }
  .canvas {
    position: relative;
    width: 1200px;
    height: 1200px;
    background: var(--backdrop);
  }
  .pouch {
    position: absolute;
    left: 254px;
    top: 101px;
    width: 618px;
    height: 949px;
    box-shadow: 0 6px 18px rgba(40, 50, 60, 0.18);
  }
  .pouch-art {
    position: absolute;
    inset: 0;
    width: 618px;
    height: 949px;
  }
  .brand-name {
    position: absolute;
    left: 420px;
    top: 182px;
    width: 130px;
    text-align: center;
    font-family: "Oswald", sans-serif;
    font-weight: 600;
    font-size: 62px;
    line-height: 1;
    color: var(--white);
  }
  .brand-slogan {
    position: absolute;
    left: 400px;
    top: 276px;
    width: 196px;
    text-align: right;
    font-family: "Roboto Condensed", sans-serif;
    font-weight: 400;
    font-size: 17px;
    line-height: 20px;
    color: var(--white);
    white-space: nowrap;
  }
  .label-space {
    position: absolute;
    left: 25px;
    top: 520px;
    width: 145px;
    height: 93px;
    box-sizing: border-box;
    background: var(--white);
    border: 1px solid #8a9098;
    border-radius: 6px;
    display: flex;
    flex-direction: column;
    justify-content: center;
    align-items: center;
    font-family: "Roboto Condensed", sans-serif;
    font-size: 12px;
    line-height: 1.35;
    color: var(--label-ink);
  }
  .product-lineup {
    position: absolute;
    left: 64px;
    top: 690px;
    width: 258px;
    height: 222px;
    border-radius: 20px;
    background: radial-gradient(ellipse at center, rgba(255,255,255,0.55), rgba(255,255,255,0.18) 70%);
  }
  .headline {
    position: absolute;
    left: 330px;
    top: 794px;
    width: 290px;
    text-align: center;
    font-family: "Oswald", sans-serif;
    font-weight: 600;
    font-size: 40px;
    line-height: 48px;
    letter-spacing: 1px;
    color: var(--white);
  }
</style>
</head>
<body>
<div class="canvas">
  <div class="pouch">
    <svg class="pouch-art" viewBox="0 0 618 949" xmlns="http://www.w3.org/2000/svg" aria-hidden="true">
      <defs>
        <linearGradient id="redBand" x1="0" y1="0" x2="0" y2="1">
          <stop offset="0" stop-color="var(--red-deep)"/>
          <stop offset="1" stop-color="var(--red)"/>
        </linearGradient>
        <linearGradient id="clearWindow" x1="0" y1="0" x2="1" y2="1">
          <stop offset="0" stop-color="var(--window)"/>
          <stop offset="0.5" stop-color="var(--window-light)"/>
          <stop offset="1" stop-color="var(--window)"/>
        </linearGradient>
        <linearGradient id="blueBand" x1="0" y1="0" x2="0" y2="1">
          <stop offset="0" stop-color="var(--blue)"/>
          <stop offset="1" stop-color="var(--blue-deep)"/>
        </linearGradient>
      </defs>
      <rect class="view-window" x="0" y="0" width="618" height="949" fill="url(#clearWindow)"/>
      <path class="red-band" d="M0 0 H618 V400 C580 390 530 360 466 310 C380 230 300 170 180 170 C110 170 60 190 0 213 Z" fill="url(#redBand)"/>
      <path class="red-edge" d="M618 400 C580 390 530 360 466 310 C380 230 300 170 180 170 C110 170 60 190 0 213" fill="none" stroke="var(--white)" stroke-width="3" opacity="0.85"/>
      <path class="blue-band" d="M0 525 C160 560 300 700 470 735 C540 748 590 746 618 742 V949 H0 Z" fill="url(#blueBand)"/>
      <path class="blue-edge" d="M0 525 C160 560 300 700 470 735 C540 748 590 746 618 742" fill="none" stroke="var(--white)" stroke-width="3" opacity="0.85"/>
      <circle class="hang-hole" cx="305" cy="50" r="12" fill="var(--backdrop)"/>
    </svg>
    <div class="brand-name">816</div>
    <div class="brand-slogan">816 Original Parts</div>
    <div class="label-space"><span>4 x 7 cm</span><span>white box</span></div>
    <div class="product-lineup" role="img" aria-label="Line drawings of five rubber suspension parts: bushings and mounts"></div>
    <div class="headline">HIGH QUALITY<br>AUTO PARTS</div>
  </div>
</div>
</body>
</html>
```